Word Studio Lindqvara Templates

We run a large number of businesses, including schools, airports, hotels and offices. We write reports on a daily basis and are looking for a strong and sexy WORD Template. We already have a logo in place (see graphical chart attached), that is rights' protected. We are looking for a beautiful wich reflect modern design and human aspects. Our logo has 2 design, full fill and watermark. It can be used in red or black.

Target Market(s)

Architects, Fire brigade, Building investors, contactors

Font styles to use
Other font styles liked:
• Arial, Calibri, ...

Requirements
Must have
• Cover page, summary, Bullet points, Tables, Figures, Annex

```html
<!DOCTYPE html>
<html lang="en">
<head>
<meta charset="utf-8">
<title>Studio Lindqvara – Report Template</title>
<link href="https://fonts.googleapis.com/css2?family=Ubuntu:wght@400;500&display=swap" rel="stylesheet">
<style>
  :root {
    --backdrop: #d8dcde;
    --paper: #ffffff;
    --brand-red: #e43a36;
    --ink: #1f1f1f;
    --rule: #2a2a2a;
    --band: #e6e6e6;
    --leader: #555555;
  }
  * { box-sizing: border-box; margin: 0; padding: 0; }
  html, body {
    width: 1200px; height: 784px; overflow: hidden;
    background: var(--backdrop);
    font-family: "Ubuntu", Arial, sans-serif;
    color: var(--ink);
  }
  .page {
    position: absolute; left: 337px; top: 20px;
    width: 526px; height: 744px;
    background: var(--paper);
    border-bottom: 6px solid var(--brand-red);
  }
  .brand {
    position: absolute; left: 42px; top: 30px;
    display: flex; align-items: flex-start; gap: 12px;
  }
  .brand-dot {
    width: 26px; height: 26px; border-radius: 50%;
    background: var(--brand-red); margin-top: 6px;
  }
  .brand-name {
    font-size: 26px; font-weight: 500; line-height: 27px; color: var(--ink);
  }
  .header-rule {
    position: absolute; left: 40px; right: 40px; top: 100px;
    border-top: 1px solid var(--rule);
  }
  .contents {
    position: absolute; left: 40px; right: 40px; top: 128px;
    border-collapse: collapse; width: 446px;
    font-size: 10px;
  }
  .contents td {
    height: 28.5px; border: 1px solid var(--rule);
    border-left-width: 1px; border-right-width: 1px;
    vertical-align: middle;
  }
  .contents tr:nth-child(odd) td { background: var(--band); }
  .row-no { width: 34px; padding-left: 6px; font-size: 11px; }
  .entry { padding: 0 8px 0 14px; }
  .list-title { font-size: 13px; font-weight: 500; }
  .list-item { display: flex; align-items: center; font-size: 10px; }
  .bullet {
    width: 9px; height: 9px; border-radius: 50%;
    background: var(--brand-red); margin-right: 8px; flex: none;
  }
  .leader {
    flex: 1; border-bottom: 1px dotted var(--leader);
    margin: 0 6px; transform: translateY(3px);
  }
</style>
</head>
<body>
  <main class="page">
    <header class="brand">
      <span class="brand-dot"></span>
      <span class="brand-name">Studio<br>Lindqvara</span>
    </header>
    <div class="header-rule"></div>

    <table class="contents">
      <tr><td class="row-no">1.</td><td class="entry"></td></tr>
      <tr><td class="row-no">2.</td><td class="entry"></td></tr>
      <tr><td class="row-no">3.</td><td class="entry"></td></tr>
      <tr><td class="row-no">4.</td><td class="entry"></td></tr>
      <tr><td class="row-no">5.</td><td class="entry list-title">List of Figures:</td></tr>
      <tr><td class="row-no">6.</td><td class="entry"><div class="list-item"><span class="bullet"></span>Dummy Figure 1:<span class="leader"></span>2</div></td></tr>
      <tr><td class="row-no">7.</td><td class="entry"><div class="list-item"><span class="bullet"></span>Dummy Figure 2:<span class="leader"></span>2</div></td></tr>
      <tr><td class="row-no">8.</td><td class="entry"><div class="list-item"><span class="bullet"></span>Dummy Figure 3:<span class="leader"></span>2</div></td></tr>
      <tr><td class="row-no">9.</td><td class="entry"></td></tr>
      <tr><td class="row-no">10.</td><td class="entry list-title">List of Tables:</td></tr>
      <tr><td class="row-no">11.</td><td class="entry"><div class="list-item"><span class="bullet"></span>Dummy Table 1:<span class="leader"></span>2</div></td></tr>
      <tr><td class="row-no">12.</td><td class="entry"><div class="list-item"><span class="bullet"></span>Dummy Table 2:<span class="leader"></span>2</div></td></tr>
      <tr><td class="row-no">13.</td><td class="entry"><div class="list-item"><span class="bullet"></span>Dummy Table 3:<span class="leader"></span>2</div></td></tr>
      <tr><td class="row-no">14.</td><td class="entry"></td></tr>
      <tr><td class="row-no">15.</td><td class="entry"></td></tr>
      <tr><td class="row-no">16.</td><td class="entry"></td></tr>
      <tr><td class="row-no">17.</td><td class="entry"></td></tr>
      <tr><td class="row-no">18.</td><td class="entry"></td></tr>
      <tr><td class="row-no">19.</td><td class="entry"></td></tr>
      <tr><td class="row-no">20.</td><td class="entry"></td></tr>
    </table>
  </main>
</body>
</html>
```